Brochure Design Project for Folk High School in Norway

We're a Folk High School placed in the south of Norway. We want help in creating a new brochure for our school next year. Check this link for the brochure for current year: http://www.brennvikskole.no/db/repository/x58301746290385716204937.pdf

We want a new design. It should not be larger than A4 size. The design dosen't need to be quadratic.

As a starting, the borchure should contain the same amount of pages and information as current brochure.

We also want access to the working-file (InDesign). We've got a lot of pictures to use, so the design template could contain more pictures.

This is a School for students in the agegroup between 18-20 years. The design must attract this group. It's a 1-year study and our focus is to give the students qualified teaching in their area of interest and great experiences linked to travelling, friendship and personal development.

As a starter, we want to see a template on a modern, playful,warm and attractive brochure. This could be shown as a PDF-file.
Updates

You can follow this link to choose among several pictures:

http://www.pixmora.example/photos/41572038@N09/

I remind you that we want access to de InDesign file... So the choose of pictures is not that important. We want for ourselves to change them. If you follow the link, you''ll find compressed pictures. But maybe they can help you in the creative process... :) We''re looking forward to see your work!

```html
<!DOCTYPE html>
<html lang="no">
<head>
<meta charset="utf-8">
<title>Brennvik Folkehøgskole – linjebrosjyre</title>
<link rel="stylesheet" href="https://fonts.googleapis.com/css2?family=Alfa+Slab+One&family=Arvo:wght@400;700&display=swap">
<style>
  :root{
    --magenta:#e6007e;
    --cyan:#00a0e3;
    --green:#3aaa35;
    --red:#d7282f;
    --ink:#0b0b0b;
    --paper:#ffffff;
    --copy:#e9e9e9;
  }
  *{box-sizing:border-box;margin:0;padding:0}
  html,body{width:1200px;height:2380px;overflow:hidden;background:var(--paper)}
  body{position:relative;font-family:"Arvo",Georgia,serif}

  .spread{position:absolute;left:76px;width:1048px;height:524px;background:var(--ink);overflow:hidden;box-shadow:0 4px 10px rgba(0,0,0,.28)}
  .spread--multisport{top:56px;--accent:var(--magenta)}
  .spread--helse{top:644px;--accent:var(--cyan)}
  .spread--fotball{top:1234px;--accent:var(--green)}
  .spread--musikk{top:1824px;--accent:var(--red)}

  .photo{position:absolute}
  .spread-shapes{position:absolute;inset:0;width:1048px;height:524px}
  .spread-shapes .header-field{fill:var(--paper)}
  .spread-shapes .accent-stripe{fill:var(--accent)}

  .brand{position:absolute;right:14px;top:16px;width:70px;text-align:right;font:700 7px/1.25 "Arvo",Georgia,serif;color:var(--accent);letter-spacing:.4px;text-transform:uppercase}
  .brand-mark{display:block;width:26px;height:26px;margin:0 0 4px auto;background:var(--accent)}

  .title{position:absolute;left:566px;top:58px;font:52px/0.95 "Alfa Slab One",Georgia,serif;color:var(--accent);letter-spacing:1px}
  .title--two-lines{top:40px;font-size:46px}
  .subtitle{position:absolute;left:568px;top:116px;font:700 17px/1 "Arvo",Georgia,serif;color:var(--ink);letter-spacing:.5px}
  .subtitle--low{top:144px}

  .band-copy{position:absolute;left:532px;top:214px;width:440px;transform:rotate(-6deg);transform-origin:0 0}
  .band-copy span{display:inline;background:var(--accent);color:#fff;font:700 10.5px/1.55 "Arvo",Georgia,serif;padding:1px 4px;box-decoration-break:clone;-webkit-box-decoration-break:clone}

  .columns{position:absolute;left:544px;top:292px;width:486px;height:196px;display:grid;grid-template-columns:150px 150px 1fr;column-gap:16px;color:var(--copy);font:400 8px/1.38 "Arvo",Georgia,serif}
  .columns p{margin-bottom:6px}
  .columns ul{list-style:none;margin-bottom:6px}
  .columns li{padding-left:8px;position:relative;margin-bottom:2px}
  .columns li::before{content:"";position:absolute;left:0;top:4px;width:3px;height:3px;background:var(--copy)}
  .col-head{font-weight:700;color:var(--accent);text-transform:uppercase;letter-spacing:.4px;margin-bottom:4px}
  .col-schedule{border-left:1px dotted var(--accent);padding-left:10px}
  .col-schedule .rule{border-top:1px dotted var(--accent);margin:6px 0}
  .highlight{color:var(--accent);font-weight:700}

  .footer{position:absolute;left:0;bottom:0;width:1048px;height:22px;background:var(--ink);color:#fff;font:700 7.5px/22px "Arvo",Georgia,serif;letter-spacing:.6px}
  .footer span{position:absolute}
  .folio-left{left:12px}
  .phone{left:300px}
  .web{left:544px}
  .folio-right{right:12px}
</style>
</head>
<body>

<!-- Multisport -->
<section class="spread spread--multisport">
  <div class="photo" role="img" aria-label="Student klatrer på en fjellvegg under blå himmel" style="left:0;top:0;width:150px;height:250px;background:linear-gradient(160deg,#3f7fd0,#8aa7b8 60%,#6b6456)"></div>
  <div class="photo" role="img" aria-label="Volleyballkamp i idrettshall" style="left:150px;top:0;width:374px;height:250px;background:linear-gradient(180deg,#2c2a26,#6e5a3a 55%,#a58a58)"></div>
  <div class="photo" role="img" aria-label="Elever med hjelmer og redningsvester klare for rafting" style="left:0;top:262px;width:250px;height:240px;background:linear-gradient(150deg,#d9c23a,#c8412c 50%,#2d3b59)"></div>
  <div class="photo" role="img" aria-label="Curlingspiller på isen" style="left:250px;top:262px;width:274px;height:240px;background:linear-gradient(170deg,#c8ccd2,#eef1f4 55%,#2a2a30)"></div>
  <svg class="spread-shapes" viewBox="0 0 1048 524" aria-hidden="true">
    <polygon class="header-field" points="524,0 1048,0 1048,152 524,208"/>
    <polygon class="accent-stripe" points="0,256 1048,146 1048,160 0,272"/>
  </svg>
  <div class="brand"><span class="brand-mark"></span>Brennvik Folkehøgskole</div>
  <h2 class="title">MUITISPORT</h2>
  <p class="subtitle">– AKTIVT OG SPENNENDE</p>
  <p class="band-copy"><span>Multisport gir deg et år fullt av spenning, utfordringer og gode sportsopplevelser. Det er stor variasjon i aktivitetene, og du er selv med og bestemmer hva vi driver med. Kort sagt: Et drømmeår!</span></p>
  <div class="columns">
    <div>
      <p>Skiløp og turer i fjellet, klatring og padling langs kysten. Her får du prøve alt fra lagspill til friluftsliv.</p>
      <ul>
        <li>Skiløp hele vinteren: alpint, telemark og langrenn</li>
        <li>Ballspill og lek: volleyball, basket, innebandy og fotball</li>
        <li>Turer ute i naturen med telt, kano, klatreutstyr og mye godt humør</li>
      </ul>
    </div>
    <div>
      <p class="col-head">Aktuelle turer:</p>
      <ul>
        <li>Fjelltur</li>
        <li>Rafting i Evje</li>
        <li>Skitur til Hovden</li>
        <li>Padling i skjærgården</li>
        <li>Klatrekurs</li>
        <li>Dykking og bading</li>
      </ul>
      <p>Linjeavgift:<br>ca. 14 000 kroner</p>
    </div>
    <div class="col-schedule">
      <p class="col-head">Timefordeling</p>
      <p>Linjefag (ca. 15 t/u)<br>• Praktisk sport og idrett<br>• Turer<br>• Friluftsliv</p>
      <div class="rule"></div>
      <p>Fellesfag 7 t/u<br>Seminar 4 t/u<br>Valgfag 2–4 t/u</p>
    </div>
  </div>
  <div class="footer"><span class="folio-left">14</span><span class="phone">TELEFON 38 40 52 00</span><span class="web">WWW.BRENNVIKSKOLE.NO</span><span class="folio-right">15</span></div>
</section>

<!-- Helse og velvære -->
<section class="spread spread--helse">
  <div class="photo" role="img" aria-label="Elever på trening i gymsal" style="left:0;top:0;width:260px;height:110px;background:linear-gradient(170deg,#c9b79c,#8c6d4f)"></div>
  <div class="photo" role="img" aria-label="Massasje av en elevs rygg" style="left:260px;top:0;width:264px;height:160px;background:linear-gradient(160deg,#f2e6da,#d9a888 60%,#b77c5e)"></div>
  <div class="photo" role="img" aria-label="To elever som ler sammen på gulvet i idrettshallen" style="left:0;top:110px;width:524px;height:392px;background:linear-gradient(165deg,#b35a2c,#e0a264 45%,#7a3f22)"></div>
  <svg class="spread-shapes" viewBox="0 0 1048 524" aria-hidden="true">
    <polygon class="header-field" points="524,0 1048,0 1048,152 524,208"/>
    <polygon class="accent-stripe" points="0,256 1048,146 1048,160 0,272"/>
  </svg>
  <div class="brand"><span class="brand-mark"></span>Brennvik Folkehøgskole</div>
  <h2 class="title title--two-lines">HELSE OG<br>VELVAERE</h2>
  <p class="subtitle subtitle--low">– FEEL GOOD</p>
  <p class="band-copy"><span>Dette er året med DEG i fokus! Lær kroppen din bedre å kjenne. Bruk et år på å prioritere deg selv og finn nye måter å oppleve fysisk velvære på. Massasje, riktig kosthold og rolig trening, for et liv i balanse.</span></p>
  <div class="columns">
    <div>
      <p>Denne linjen handler om å lære å ta vare på seg selv. Her får du bygge styrke og overskudd i hverdagen.</p>
      <ul>
        <li>Du lærer enkel massasje og avspenning</li>
        <li>Vi trener yoga, pilates og styrke</li>
        <li>Matlaging med sunne råvarer</li>
      </ul>
      <p>Studietur til <span class="highlight">Barcelona</span>.</p>
    </div>
    <div>
      <ul>
        <li>Samtaler om trivsel og livsstil</li>
        <li>Natur og ro: turer, bad og stillhet</li>
        <li>Forstå hvordan kroppen henger sammen med tankene</li>
      </ul>
      <p>Et år fylt med trening, glede og nye venner som gir deg ny energi.</p>
      <p>Linjeavgift:<br>ca. 7 000 kroner</p>
    </div>
    <div class="col-schedule">
      <p class="col-head">Timefordeling</p>
      <p>Linjefag (ca. 15 t/u)<br>• Aromamassasje<br>• Trening<br>• Mat og ernæring<br>• Psykologi<br>• Anatomi</p>
      <div class="rule"></div>
      <p>Fellesfag 7 t/u<br>Seminar 4 t/u<br>Valgfag 2–4 t/u</p>
    </div>
  </div>
  <div class="footer"><span class="folio-left">18</span><span class="phone">TELEFON 38 40 52 00</span><span class="web">WWW.BRENNVIKSKOLE.NO</span><span class="folio-right">19</span></div>
</section>

<!-- Fotball -->
<section class="spread spread--fotball">
  <div class="photo" role="img" aria-label="Fotballspillere i kamp på gressbanen" style="left:0;top:0;width:150px;height:120px;background:linear-gradient(170deg,#6d8f55,#3f7a34)"></div>
  <div class="photo" role="img" aria-label="Lagbilde av fotballaget i røde drakter" style="left:150px;top:0;width:374px;height:150px;background:linear-gradient(175deg,#8fae72,#b7342f 55%,#3f7a34)"></div>
  <div class="photo" role="img" aria-label="Supportere på tribunen foran et stort fotballstadion" style="left:0;top:120px;width:524px;height:382px;background:linear-gradient(180deg,#1c3a20,#3f8a3a 40%,#a8402f 75%,#3a1e16)"></div>
  <svg class="spread-shapes" viewBox="0 0 1048 524" aria-hidden="true">
    <polygon class="header-field" points="524,0 1048,0 1048,152 524,208"/>
    <polygon class="accent-stripe" points="0,256 1048,146 1048,160 0,272"/>
  </svg>
  <div class="brand"><span class="brand-mark"></span>Brennvik Folkehøgskole</div>
  <h2 class="title">FOTBALL</h2>
  <p class="subtitle">– DET DU LIKER BEST</p>
  <p class="band-copy"><span>Digger du fotball? Føles det godt å være i aktivitet og presse grensene i banen? Dette er muligens den ultimate linjen for akkurat deg! Fotball står i fokus, men også kryddret med andre spennende aktiviteter. Det er slettes ikke noe krav å gå glipp av dette!</span></p>
  <div class="columns">
    <div>
      <p>Velger du denne linjen, får du disse opplevelsene med på kjøpet:</p>
      <ul>
        <li>Mange og varierte treningsøkter med fokus på teknikk og samspill</li>
        <li>Egen kamptropp og turneringer mot andre skoler</li>
        <li>Trening sammen med lokale klubber</li>
        <li>Trenerkurs og dommerkurs</li>
      </ul>
    </div>
    <div>
      <ul>
        <li>Vi samarbeider med lokale klubber om hospitering</li>
        <li>Klubbesøk i England, med kamp og omvisning</li>
        <li>Kosthold og restitusjon</li>
        <li>Skikkelig lagånd på og utenfor banen</li>
      </ul>
      <p>Linjeavgift:<br>ca. 18 400 kroner</p>
    </div>
    <div class="col-schedule">
      <p class="col-head">Timefordeling</p>
      <p>Linjefag (ca. 15 t/u)<br>• Praktisk fotball<br>• Teori<br>• Trenerlære</p>
      <div class="rule"></div>
      <p class="col-head">Aktiviteter</p>
      <p>Fotballtur til England<br>Cuper og turneringer<br>Fotballdag i nærmiljøet</p>
      <div class="rule"></div>
      <p>Fellesfag 7 t/u<br>Seminar 4 t/u<br>Valgfag 2–4 t/u</p>
    </div>
  </div>
  <div class="footer"><span class="folio-left">16</span><span class="phone">TELEFON 38 40 52 00</span><span class="web">WWW.BRENNVIKSKOLE.NO</span><span class="folio-right">17</span></div>
</section>

<!-- Musikk -->
<section class="spread spread--musikk">
  <div class="photo" role="img" aria-label="Elever som spiller gitar i øvingsrommet" style="left:0;top:0;width:190px;height:140px;background:linear-gradient(160deg,#3b2a24,#8a5a40)"></div>
  <div class="photo" role="img" aria-label="Sanger på scenen i rødt lys" style="left:190px;top:0;width:150px;height:140px;background:linear-gradient(170deg,#1a0d10,#b0202a 60%,#3b0c12)"></div>
  <div class="photo" role="img" aria-label="Elev som spiller keyboard" style="left:340px;top:0;width:184px;height:140px;background:linear-gradient(160deg,#d9c7b0,#6c5647)"></div>
  <div class="photo" role="img" aria-label="Gitarist foran et bål i mørket" style="left:0;top:140px;width:524px;height:362px;background:radial-gradient(ellipse at 30% 60%,#ffb347,#d2561c 35%,#5a1e0c 65%,#140706)"></div>
  <svg class="spread-shapes" viewBox="0 0 1048 524" aria-hidden="true">
    <polygon class="header-field" points="524,0 1048,0 1048,152 524,208"/>
    <polygon class="accent-stripe" points="0,256 1048,146 1048,160 0,272"/>
  </svg>
  <div class="brand"><span class="brand-mark"></span>Brennvik Folkehøgskole</div>
  <h2 class="title">MUSIKK</h2>
  <p class="subtitle">– DITT TALENT, VÅR BEGEISTRING</p>
  <p class="band-copy"><span>Ønsker du et år med nye tid til å jobbe med musikk? På Musikk står du og dine ønsker i fokus. Vi tilbyr band, musikkteori, instrument og samspill. Her får du tid til å finne din egen stil, og du velger selv hva du vil bli flink til.</span></p>
  <div class="columns">
    <div>
      <p>Du er selv med og bestemmer hvordan året blir. Sammen lager vi en plan som passer deg.</p>
      <ul>
        <li>Faste øvinger med band</li>
        <li>Lær å bruke studio og lydutstyr</li>
        <li>Få hjelp til låtskriving</li>
        <li>Spill for publikum</li>
      </ul>
      <p>Vi har et godt øvingsrom, nytt studio og en stor scene.</p>
    </div>
    <div>
      <p>Studieturen til <span class="highlight">New York</span> er en av årets høydepunkter, med konserter og besøk hos musikere.</p>
      <p>Vi lager egne konserter gjennom hele året, både på skolen og ute i byen.</p>
      <p>Linjeavgift:<br>ca. 17 000 kroner</p>
    </div>
    <div class="col-schedule">
      <p class="col-head">Timefordeling</p>
      <p>Linjefag (ca. 15 t/u)<br>• Samspill<br>• Musikkteori<br>• Låtskriving<br>• Studioarbeid<br>• Konserter</p>
      <div class="rule"></div>
      <p>Fellesfag 7 t/u<br>Seminar 4 t/u<br>Valgfag 2–4 t/u</p>
    </div>
  </div>
  <div class="footer"><span class="folio-left">12</span><span class="phone">TELEFON 38 40 52 00</span><span class="web">WWW.BRENNVIKSKOLE.NO</span><span class="folio-right">13</span></div>
</section>

</body>
</html>
```